Dust N Gone! Cleaning needs a flyer!

We have started a cleaning business DUST N GONE! Cleaning, and had a new logo design for it.
We would like a flyer designed to present to businesses that represents our professionalism, quality of service, security and value for money.
We would like a flyer that we can present to both our residential clients and business owners alike.
We will use this flyer for the next 2 years without having to make changes.
I'm happy for the designer to come up with their own wording if necessary.
Updates

Hello everyone!

In addition to the information I have already provided, please see below for more information to be included on the design for our flyer.

Thank you in advance.

Don’t read this unless your current cleaners are AMAZING!

Are you still reading? Now for the good news! Announcing the arrival of the amazing cleaning team of Dust N Gone! Cleaning. They’re the BEST in the Wimmera and we personally guarantee it.

We offer an ultimate service that NO other cleaning company in the Wimmera can offer; high quality cleaning of your home or business, carpet dry cleaning and pest control. All of these services can be completed at a time that is most convenient to you.

From wiping benches to washing windows, from dusting skirting boards to dry cleaning your carpets, from bathrooms to bugs, we really are your ONE stop shop.

Why choose the greatest cleaning company in the Wimmera?

For over 18 years, we have built a reputation on honesty and trust in the residential and commercial services. Our business is to know what people expect when we walk in to your home or business.

With our vast experience and knowledge, we know how to find the best people for the job, how to identify the best products for the clean, we use the newest of technology and equipment and have the best attitudes in town.

Local people, local business that you can rely on because we are also Dust N Gone! Pest Control & Fibrelux all rolled in to your ONE stop shop for residential services.

Call us to discuss how we can give you the quality you demand.

Residential Cleaning                                                       Commercial Cleaning                                     

General house cleaning                                                  Business Premises          

Home help                                                                         Vacated properties

Rental vacancies                                                               Schools

Post renovation cleans                                                     Motels/Hotels

 

                                   

Target Market(s)

Business owners, commercial properties, home owners (women aged between 30 - 80y/o)

Industry/Entity Type

Residential

Requirements
Must have
• Incorporate our logo and colours.
Double sided.
Images of interiors of both home & office.
Catch phrase: "You demand quality ..... we guarantee it!"
Address: 22-26 Mallowdene St, Horsham VIC 3400
Phone: 1300 482 316
ABN: 47 385 602 139
We complete the ususal cleaning such as:
General House cleaning
Commercial Cleaning
Rental Properties
Business Premises
Other services we offer is:
Carpet dry cleaning
Upholstery cleaning
Dust N Gone! Critter Chasers pest control
Window cleaning.

```html
<!DOCTYPE html>
<html lang="en">
<head>
<meta charset="utf-8">
<title>Dust N Gone! Cleaning – Flyer</title>
<link rel="stylesheet" href="https://fonts.googleapis.com/css2?family=Carlito:ital,wght@0,700;1,700&family=Open+Sans:wght@400;600&display=swap">
<style>
  :root {
    --ink: #000000;
    --paper: #ffffff;
    --magenta: #e624d2;
    --magenta-soft: #f04fe0;
    --magenta-deep: #b5129f;
    --text-dark: #111111;
    --contact: #f4f4f4;
  }
  * { margin: 0; padding: 0; box-sizing: border-box; }
  html, body {
    width: 879px;
    height: 1200px;
    overflow: hidden;
    background: var(--ink);
  }
  .flyer {
    position: relative;
    width: 879px;
    height: 1200px;
    overflow: hidden;
    background: var(--ink);
    font-family: "Open Sans", Arial, sans-serif;
  }
  .backdrop {
    position: absolute;
    inset: 0;
    width: 879px;
    height: 1200px;
  }
  .brand-name {
    position: absolute;
    left: 18px;
    top: 150px;
    width: 410px;
    font-family: "Open Sans", Arial, sans-serif;
    font-weight: 600;
    font-size: 54px;
    line-height: 62px;
    color: var(--paper);
    letter-spacing: 1px;
  }
  .contact {
    position: absolute;
    font-family: "Carlito", Calibri, sans-serif;
    font-weight: 700;
    font-size: 30px;
    line-height: 32px;
    letter-spacing: -0.5px;
    color: var(--contact);
    text-shadow: -1px -1px 0 #000, 1px -1px 0 #000, -1px 1px 0 #000, 2px 2px 2px #000, 0 0 4px #555;
  }
  .contact--address { left: 523px; top: 54px; }
  .contact--phone { left: 526px; top: 166px; }
  .contact--abn { left: 527px; top: 252px; }
  .abn-label {
    position: absolute;
    left: 433px;
    top: 250px;
    font-family: "Carlito", Calibri, sans-serif;
    font-weight: 700;
    font-size: 33px;
    color: var(--magenta-soft);
    text-shadow: 0 0 6px var(--magenta), 0 0 2px var(--magenta);
  }
  .service {
    position: absolute;
    font-size: 35px;
    line-height: 40px;
    color: var(--text-dark);
    white-space: pre;
  }
  .service--left { left: 84px; }
  .service--right { left: 539px; }
  .extras {
    position: absolute;
    left: 70px;
    top: 852px;
    width: 300px;
    font-family: "Carlito", Calibri, sans-serif;
    font-style: italic;
    font-weight: 700;
    font-size: 26px;
  }
  .extras__heading {
    color: var(--text-dark);
    line-height: 35px;
  }
  .extras__heading span { display: block; padding-left: 37px; }
  .extras__list { list-style: none; color: var(--magenta); }
  .extras__item { position: absolute; left: 0; line-height: 29px; }
  .promise {
    position: absolute;
    left: 518px;
    top: 925px;
    width: 346px;
    text-align: center;
    font-family: "Carlito", Calibri, sans-serif;
    font-weight: 700;
    color: var(--paper);
  }
  .promise__demand { font-size: 32px; line-height: 38px; }
  .promise__guarantee { font-size: 40px; line-height: 46px; margin-top: 16px; }
</style>
</head>
<body>
<main class="flyer">
  <svg class="backdrop" viewBox="0 0 750 1024" preserveAspectRatio="none" aria-hidden="true">
    <defs>
      <filter id="glow" x="-50%" y="-50%" width="200%" height="200%">
        <feGaussianBlur stdDeviation="3" result="b"/>
        <feMerge><feMergeNode in="b"/><feMergeNode in="SourceGraphic"/></feMerge>
      </filter>
      <linearGradient id="line-fade-h" x1="0" x2="1">
        <stop offset="0" stop-color="#e624d2" stop-opacity="0.3"/>
        <stop offset="0.5" stop-color="#f04fe0"/>
        <stop offset="1" stop-color="#e624d2" stop-opacity="0"/>
      </linearGradient>
      <linearGradient id="line-fade-v" x1="0" x2="0" y1="0" y2="1">
        <stop offset="0" stop-color="#e624d2" stop-opacity="0"/>
        <stop offset="0.4" stop-color="#f04fe0"/>
        <stop offset="1" stop-color="#e624d2" stop-opacity="0.4"/>
      </linearGradient>
      <linearGradient id="shield-fill" x1="0" x2="0" y1="0" y2="1">
        <stop offset="0" stop-color="#f04fe0"/>
        <stop offset="1" stop-color="#d21bbd"/>
      </linearGradient>
    </defs>

    <!-- white content area -->
    <path d="M0,300 C180,272 480,262 750,388 L750,945 C560,1010 300,1000 0,992 Z" fill="#ffffff"/>
    <!-- magenta swoosh -->
    <path d="M0,318 C260,288 520,300 716,378 C520,330 260,332 0,380 Z" fill="#e624d2"/>

    <!-- glowing frame lines -->
    <g filter="url(#glow)" stroke-width="3">
      <line x1="38" y1="630" x2="38" y2="1024" stroke="url(#line-fade-v)"/>
      <line x1="0" y1="715" x2="400" y2="715" stroke="url(#line-fade-h)"/>
      <line x1="315" y1="700" x2="315" y2="1005" stroke="url(#line-fade-v)"/>
      <line x1="0" y1="990" x2="390" y2="990" stroke="url(#line-fade-h)"/>
    </g>

    <!-- address icon: house -->
    <g filter="url(#glow)" stroke="#f04fe0" stroke-width="4" fill="none" stroke-linejoin="round">
      <path d="M370,68 L404,40 L438,68"/>
      <rect x="378" y="64" width="52" height="34" fill="#1a0016"/>
      <rect x="386" y="72" width="12" height="10" fill="#f04fe0" stroke="none"/>
      <rect x="410" y="72" width="12" height="10" fill="#f04fe0" stroke="none"/>
      <rect x="398" y="84" width="12" height="14" fill="#f04fe0" stroke="none"/>
    </g>

    <!-- phone icon -->
    <g filter="url(#glow)">
      <rect x="374" y="128" width="56" height="56" rx="10" fill="#e624d2"/>
      <path d="M392,138 C386,146 388,162 398,172 C406,180 414,180 420,176 L414,166 L408,168 C402,164 398,158 398,152 L403,148 Z" fill="#ffffff"/>
    </g>

    <!-- promise shield -->
    <path d="M442,763 Q590,742 742,763 L736,862 Q722,952 590,992 Q458,952 446,862 Z" fill="url(#shield-fill)" stroke="#f77ce9" stroke-width="3" filter="url(#glow)"/>
  </svg>

  <h1 class="brand-name">Dust N Gone!<br>Cleaning</h1>

  <p class="contact contact--address">22-26 Mallowdene St, Horsham<br>VIC 3400</p>
  <p class="contact contact--phone">1300 482 316</p>
  <span class="abn-label">ABN</span>
  <p class="contact contact--abn">47 385 602 139</p>

  <section class="services" aria-label="Cleaning services">
    <p class="service service--left" style="top:441px">Residential Cleaning</p>
    <p class="service service--right" style="top:441px">Commercial</p>
    <p class="service service--left" style="top:487px">Cleaning</p>
    <p class="service service--left" style="top:531px">General House Cleaning</p>
    <p class="service service--right" style="top:531px">Business</p>
    <p class="service service--left" style="top:579px">Premises</p>
    <p class="service service--left" style="top:623px">Home  help</p>
    <p class="service service--right" style="top:623px;left:543px">Vacated</p>
    <p class="service service--left" style="top:670px">properties</p>
    <p class="service service--left" style="top:718px">Rental Vacancies</p>
    <p class="service service--right" style="top:718px">Schools</p>
    <p class="service service--left" style="top:776px">Post Renovation cleans</p>
    <p class="service service--right" style="top:776px">Motels/Hotels</p>
  </section>

  <section class="extras">
    <h2 class="extras__heading">Other Services we<span>offer are:</span></h2>
    <ul class="extras__list">
      <li class="extras__item" style="top:88px">Carpet dry cleaning</li>
      <li class="extras__item" style="top:142px">Upholstery cleaning</li>
      <li class="extras__item" style="top:196px">Dust N Gone! Critter Chasers<br>pest control</li>
      <li class="extras__item" style="top:280px">Window Cleaning</li>
    </ul>
  </section>

  <div class="promise">
    <p class="promise__demand">You demand<br>Quality</p>
    <p class="promise__guarantee">We guarantee<br>it!</p>
  </div>
</main>
</body>
</html>
```